VintnerLoop Restuarant Postcard

I have a list of restaurant owners that I need to get to take Action on my Website.

The Website is:

http://www.vintnerloop.example

The goal of the Post card will be to mail to Restaurant Owners and encourage them to visit our Website and enter some details about their property on our website.

The Card Must Contain the Text:

Get New Customers From:

www.VintnerLoop.example

admin@vintnerloop.example

555-417-2096

The steps I need recipients of the card to take

1. Visit: www.VintnerLoop.example

2. Find your Restaurant using the Search Box

3. Click on Restaurant

4. Click on “Do You”

5. Enter your Corkage Fee Details!

I have loaded a some files:

I added some Logos, as well as some screenshots of my attempts at the post card.

Industry/Entity Type

Restaurant

```html
<!DOCTYPE html>
<html lang="en">
<head>
<meta charset="utf-8">
<title>VintnerLoop Restaurant Postcard</title>
<link rel="stylesheet" href="https://fonts.googleapis.com/css2?family=Cinzel:wght@400;700&family=Questrial&family=EB+Garamond&display=swap">
<style>
  :root {
    --ink: #1a1a1a;
    --wine: #8c1c22;
    --paper: #ffffff;
    --frame: #8a8a8a;
    --photo-light: #d6d6d6;
    --photo-dark: #6e6e6e;
    --icon-wood: #8a5a2e;
    --icon-wood-dark: #5b3617;
    --icon-line: #f3e6d3;
  }
  html, body {
    margin: 0;
    width: 716px;
    height: 1200px;
    overflow: hidden;
    background: var(--paper);
  }
  .canvas {
    position: relative;
    width: 716px;
    height: 1200px;
    color: var(--ink);
    font-family: "Cinzel", serif;
  }
  .card {
    position: absolute;
    left: 0;
    width: 714px;
    border: 1px solid var(--frame);
    background: var(--paper);
    overflow: hidden;
  }
  .card--front { top: 0; height: 548px; }
  .card--back { top: 648px; height: 550px; }

  .brand {
    position: absolute;
    display: flex;
    align-items: center;
    gap: 10px;
    font-family: "Questrial", sans-serif;
    color: var(--ink);
    letter-spacing: 0.5px;
  }
  .brand__mark {
    width: 14px;
    height: 14px;
    background: var(--ink);
  }
  .card--front .brand { left: 40px; top: 46px; font-size: 48px; }
  .card--back .brand { left: 62px; top: 672px; top: 24px; font-size: 44px; }

  .front__copy { position: absolute; left: 0; top: 0; width: 470px; }
  .front__line { position: absolute; margin: 0; white-space: nowrap; }
  .lead { left: 36px; top: 162px; font-size: 25px; letter-spacing: 1px; }
  .site { left: 58px; top: 218px; font-size: 25px; letter-spacing: 0.5px; }
  .email { left: 36px; top: 276px; font-size: 24px; color: var(--wine); }
  .phone { left: 76px; top: 318px; font-family: "EB Garamond", serif; font-size: 40px; }
  .pitch {
    position: absolute;
    left: 20px;
    top: 384px;
    width: 440px;
    margin: 0;
    text-align: center;
    font-size: 21px;
    line-height: 28px;
  }
  .pitch strong { font-weight: 700; }

  .collage { position: absolute; left: 446px; top: 0; width: 270px; height: 548px; }
  .collage__band { position: absolute; left: 56px; top: 0; width: 127px; height: 548px; background: var(--wine); }
  .photo {
    position: absolute;
    background: linear-gradient(135deg, var(--photo-light), var(--photo-dark));
  }

  .directory__title {
    position: absolute;
    left: 22px;
    top: 112px;
    margin: 0;
    font-size: 25px;
    font-weight: 700;
    letter-spacing: 0.5px;
  }
  .steps { position: absolute; left: 62px; top: 154px; margin: 0; padding: 0; list-style: none; }
  .step {
    display: flex;
    align-items: center;
    height: 48px;
    margin-bottom: 9px;
    font-size: 18px;
  }
  .step__icon { width: 47px; height: 47px; margin-right: 16px; flex: none; }
</style>
</head>
<body>
<div class="canvas">

  <section class="card card--front">
    <div class="brand"><span class="brand__mark"></span>VintnerLoop</div>
    <div class="front__copy">
      <p class="front__line lead">Get New Customers From:</p>
      <p class="front__line site">www.VintnerLoop.example</p>
      <p class="front__line email">admin@vintnerloop.example</p>
      <p class="front__line phone">555-417-2096</p>
      <p class="pitch">Connoisseurs and frugal<br>customers are using our<br>site to find resurants<br>with good corkage policies.<br><strong>Be on that list!</strong></p>
    </div>
    <div class="collage">
      <div class="collage__band"></div>
      <div class="photo" style="left:92px;top:0;width:142px;height:118px" role="img" aria-label="Black and white photo of a hand at a dining table"></div>
      <div class="photo" style="left:183px;top:0;width:87px;height:82px" role="img" aria-label="Photo of a wine glass"></div>
      <div class="photo" style="left:20px;top:95px;width:164px;height:109px;background:linear-gradient(135deg,#e2e2e2,#8a1a20 55%,#3a3a3a)" role="img" aria-label="Photo of a glass of red wine"></div>
      <div class="photo" style="left:92px;top:176px;width:142px;height:88px" role="img" aria-label="Black and white photo of a marble surface"></div>
      <div class="photo" style="left:16px;top:264px;width:149px;height:109px" role="img" aria-label="Photo of a wine bottle, glass and grapes"></div>
      <div class="photo" style="left:143px;top:338px;width:127px;height:98px" role="img" aria-label="Black and white photo of a set restaurant table"></div>
      <div class="photo" style="left:2px;top:429px;width:153px;height:109px;background:linear-gradient(135deg,#cfcfcf,#7a4a3a 60%,#4a4a4a)" role="img" aria-label="Photo of bread, cheese and tomatoes"></div>
    </div>
  </section>

  <section class="card card--back">
    <div class="brand" style="left:62px"><span class="brand__mark"></span>VintnerLoop</div>
    <h2 class="directory__title">Get Listed in Our Free Directory</h2>
    <ol class="steps">
      <li class="step">
        <svg class="step__icon" viewBox="0 0 47 47" aria-hidden="true"><rect width="47" height="47" rx="6" fill="var(--icon-wood)" stroke="var(--icon-wood-dark)" stroke-width="2"/><g fill="none" stroke="var(--icon-line)" stroke-width="2"><circle cx="23.5" cy="23.5" r="14"/><ellipse cx="23.5" cy="23.5" rx="6" ry="14"/><line x1="9.5" y1="23.5" x2="37.5" y2="23.5"/><path d="M12 16h23M12 31h23"/></g></svg>
        Visit www.VintnerLoop.example
      </li>
      <li class="step">
        <svg class="step__icon" viewBox="0 0 47 47" aria-hidden="true"><rect width="47" height="47" rx="6" fill="var(--icon-wood)" stroke="var(--icon-wood-dark)" stroke-width="2"/><g fill="none" stroke="var(--icon-line)" stroke-width="3"><circle cx="20" cy="20" r="9"/><line x1="27" y1="27" x2="37" y2="37" stroke-linecap="round"/></g></svg>
        Find your Restaurant
      </li>
      <li class="step">
        <svg class="step__icon" viewBox="0 0 47 47" aria-hidden="true"><rect width="47" height="47" rx="6" fill="var(--icon-wood)" stroke="var(--icon-wood-dark)" stroke-width="2"/><path d="M15 10 L15 35 L21 29 L26 38 L30 36 L25 27 L33 27 Z" fill="var(--icon-line)"/></svg>
        Click on Restaurant
      </li>
      <li class="step">
        <svg class="step__icon" viewBox="0 0 47 47" aria-hidden="true"><rect width="47" height="47" rx="6" fill="var(--icon-wood)" stroke="var(--icon-wood-dark)" stroke-width="2"/><g fill="none" stroke="var(--icon-line)" stroke-width="3" stroke-linecap="round"><path d="M17 17a6.5 6.5 0 1 1 9 6c-2 1-2.5 2.5-2.5 5"/></g><circle cx="23.5" cy="35" r="2" fill="var(--icon-line)"/></svg>
        Click on “Do You”
      </li>
      <li class="step">
        <svg class="step__icon" viewBox="0 0 47 47" aria-hidden="true"><rect width="47" height="47" rx="6" fill="var(--icon-wood)" stroke="var(--icon-wood-dark)" stroke-width="2"/><rect x="11" y="13" width="23" height="23" fill="none" stroke="var(--icon-line)" stroke-width="2.5"/><path d="M15 24l6 6 13-17" fill="none" stroke="var(--icon-line)" stroke-width="3" stroke-linecap="round" stroke-linejoin="round"/></svg>
        Enter your Details!
      </li>
    </ol>
  </section>

</div>
</body>
</html>
```